Inflatable Event Hirer requires Tri-Fold mini brochure

Brochure design required for UK based entertainment company offering a wide range of entertainment equipment for a broad range of customers including private customers, corporate customers and charities. Brochure must showcase a overview of our products including most popular products and unique items such as Bouncy Castles, Obstacle Courses, Slides, Rodeo Bulls and Dunk Tanks that are available for hire for a wide range of events including Birthdays, weddings, festivals, product launches and more. Brochure design idea's to compliment existing website design www.hopvalleyleisure.co.uk Brochure needs to be highly visual with wording kept minimal with easy read at forefront of design.

Target Market(s)

Young Families, young adults, schools.

Industry/Entity Type

Entertainment

Requirements
Must have
• An overview of our products we offer;
• Bouncy Castle
• Inflatable Slides
• Obstacle Courses
• Go Karts
• Climbing Walls
• Candy Carts *NEW*
• Mobile Bars *NEW*
• Trampolines
• Rodeo Bulls
• Dunk Tanks
• and much more....
• Emphasis on website/online booking/telephone number (0871 4956 382)
• UK Nationwide delivery with most European countries covered.
• £5 million public liability insurance as standard!
• BLPG accredited company
• WKSC accredited staff
Nice to have
• Pictures of events/parties etc.

```html
<!DOCTYPE html>
<html lang="en">
<head>
<meta charset="utf-8">
<title>Hop Valley Leisure – Tri-Fold Brochure</title>
<link href="https://fonts.googleapis.com/css2?family=Bungee&family=Open+Sans:wght@700;800&display=swap" rel="stylesheet">
<style>
  :root {
    --red: #e11f2b;
    --green: #1fa84a;
    --lime: #8cc63f;
    --magenta: #c2187f;
    --yellow: #dfe21f;
    --cyan: #14a3c7;
    --purple: #9b2a8e;
    --teal: #14a99a;
    --leaf: #8dc63f;
    --orange: #f26522;
    --plum: #8e1f6b;
    --grass: #3aae49;
    --white: #ffffff;
    --page: #efefef;
  }
  * { box-sizing: border-box; margin: 0; padding: 0; }
  html, body { width: 1200px; height: 1000px; overflow: hidden; background: var(--page); }
  .brochure {
    position: absolute; left: 48px; top: 108px; width: 1104px; height: 782px;
    overflow: hidden; font-family: "Open Sans", Arial, sans-serif; color: var(--white);
    box-shadow: 0 4px 14px rgba(0,0,0,.25);
  }
  .backdrop { position: absolute; inset: 0; }
  .panel {
    position: absolute; border: 4px solid var(--white); border-radius: 34px;
    font-weight: 700; font-size: 13.4px; line-height: 17.4px;
  }
  .panel--reliability { left: 32px; top: 80px; width: 302px; height: 150px; background: var(--teal); border-left: none; border-top: none; padding: 14px 16px 0 26px; border-radius: 0 34px 34px 0; }
  .panel--satisfaction { left: 36px; top: 294px; width: 296px; height: 468px; background: var(--leaf); padding: 42px 20px 0 24px; border-radius: 28px 34px 34px 34px; }
  .panel--satisfaction p + p { margin-top: 17px; }
  .panel--credentials { left: 407px; top: 77px; width: 292px; height: 288px; background: var(--orange); padding: 30px 10px 0; text-align: center; font-size: 16.5px; line-height: 22px; border-radius: 34px; }
  .panel--credentials p + p { margin-top: 22px; }
  .heading {
    position: absolute; font-family: "Bungee", Impact, sans-serif; font-size: 24px; line-height: 26px;
    background: var(--white); color: var(--leaf); padding: 0 3px;
  }
  .heading--reliability { left: 150px; top: 48px; }
  .heading--satisfaction { left: 116px; top: 268px; text-align: right; color: var(--leaf); }
  .heading--satisfaction span { display: block; }
  .crowd { position: absolute; left: 54px; top: 226px; width: 78px; height: 82px; background: linear-gradient(var(--plum), #a8407f); border-radius: 6px 6px 0 0; }
  .cta { position: absolute; left: 400px; width: 300px; text-align: center; }
  .cta__label { font-family: "Bungee", Impact, sans-serif; font-size: 22px; color: var(--white); word-spacing: 10px; }
  .cta__label span { padding: 0 3px; }
  .cta--book { top: 395px; }
  .cta--book .cta__label span { background: var(--plum); }
  .cta--book .cta__value { color: var(--plum); font-size: 24px; }
  .cta--call { top: 480px; }
  .cta--call .cta__label span { background: var(--grass); }
  .cta--call .cta__value { color: var(--grass); font-size: 26px; }
  .cta__value { font-weight: 800; margin-top: 2px; }
  .event-photo {
    position: absolute; left: 750px; top: 75px; width: 356px; height: 356px; border-radius: 50%;
    border: 7px solid var(--white);
    background: radial-gradient(circle at 45% 40%, #e9c4a4 0%, #6e97cf 45%, #5a3b2a 80%);
  }
  .brand-seal {
    position: absolute; left: 780px; top: 380px; width: 232px; height: 232px; border-radius: 50%;
    background: var(--white); display: flex; align-items: center; justify-content: center;
  }
  .brand-seal__name { font-weight: 800; font-size: 34px; color: var(--grass); }
</style>
</head>
<body>
<div class="brochure">
  <svg class="backdrop" width="1104" height="782" viewBox="0 0 1104 782" aria-hidden="true">
    <g>
      <rect x="0" width="37" height="782" fill="#e11f2b"/><rect x="37" width="37" height="782" fill="#1fa84a"/>
      <rect x="74" width="37" height="782" fill="#8cc63f"/><rect x="111" width="37" height="782" fill="#c2187f"/>
      <rect x="148" width="37" height="782" fill="#dfe21f"/><rect x="185" width="37" height="782" fill="#e11f2b"/>
      <rect x="222" width="37" height="782" fill="#1fa84a"/><rect x="259" width="37" height="782" fill="#8cc63f"/>
      <rect x="296" width="37" height="782" fill="#c2187f"/><rect x="333" width="37" height="782" fill="#dfe21f"/>
      <rect x="370" width="37" height="782" fill="#e11f2b"/><rect x="407" width="37" height="782" fill="#14a3c7"/>
      <rect x="444" width="37" height="782" fill="#9b2a8e"/><rect x="481" width="37" height="782" fill="#8cc63f"/>
      <rect x="518" width="37" height="782" fill="#c2187f"/><rect x="555" width="37" height="782" fill="#1fa84a"/>
      <rect x="592" width="37" height="782" fill="#14a3c7"/><rect x="629" width="37" height="782" fill="#8cc63f"/>
      <rect x="666" width="37" height="782" fill="#9b2a8e"/><rect x="703" width="37" height="782" fill="#dfe21f"/>
      <rect x="740" width="37" height="782" fill="#e11f2b"/><rect x="777" width="37" height="782" fill="#1fa84a"/>
      <rect x="814" width="37" height="782" fill="#8cc63f"/><rect x="851" width="37" height="782" fill="#c2187f"/>
      <rect x="888" width="37" height="782" fill="#1fa84a"/><rect x="925" width="37" height="782" fill="#e11f2b"/>
      <rect x="962" width="37" height="782" fill="#8cc63f"/><rect x="999" width="37" height="782" fill="#9b2a8e"/>
      <rect x="1036" width="37" height="782" fill="#c2187f"/><rect x="1073" width="37" height="782" fill="#dfe21f"/>
    </g>
    <path d="M0 4 C120 40 300 120 420 200 C520 150 640 120 760 110 L1104 110 L1104 380
             C980 430 900 470 780 520 C640 575 480 600 320 585 C200 570 100 540 0 500 Z" fill="#ffffff"/>
  </svg>

  <h2 class="heading heading--reliability">Reliability</h2>
  <div class="panel panel--reliability">
    We are an independent company but work alongside many other hirers, so if we don't have the equipment you require, we can almost always source it from one of our recommended partners, never letting you down.
  </div>

  <div class="crowd" role="img" aria-label="Silhouettes of cheering children"></div>
  <h2 class="heading heading--satisfaction"><span>Customer</span><span>Satisfaction</span></h2>
  <div class="panel panel--satisfaction">
    <p>We believe that our success can only be measured by the success of your event and the enjoyment expressed by your guests - there is no greater reward than a happy customer! Hop Valley has achieved a 99.9% score for our services, rated at very or extremely professional for the overall experience.</p>
    <p>In comparison to our competitors, we achieved a score of 99.9% for our products being of high quality, rated from comparable to much better.</p>
    <p>Hop Valley Customer Services have been rated from very to extremely efficient and helpful at 94.8%. 100% of our customers surveyed agreed they would recommend our services to family, friends or other businesses.</p>
  </div>

  <div class="panel panel--credentials">
    <p>UK Nationwide delivery with most European countries covered</p>
    <p>£5 million public liability insurance as standard!</p>
    <p>BLPG accredited company</p>
    <p>WKSC accredited staff</p>
  </div>

  <div class="cta cta--book">
    <div class="cta__label"><span>Book</span> <span>Online</span></div>
    <div class="cta__value">hopvalleyleisure.co.uk</div>
  </div>
  <div class="cta cta--call">
    <div class="cta__label"><span>Call</span> <span>Us</span></div>
    <div class="cta__value">0871 4956 382</div>
  </div>

  <div class="event-photo" role="img" aria-label="Photo of two smiling children playing on a climbing net"></div>
  <div class="brand-seal"><span class="brand-seal__name">Hop Valley</span></div>
</div>
</body>
</html>
```